EOFYS BANNER REQUIRED FOR HIGH-END BABY PRODUCT

We seel baby beanbags, and we need a banner for our annual END OF FINANCIAL YEAR SALE (EOFYS) about 700x900px.

The promo will be:

THE EOFYS SALE IS ON NOW!
30% OFF ALL ORDERS OVER $149 WITH CODE: EOFYS

We will use this banner for an email marketing campaign, and we will actually need to resize this banner to suit some affiliate marketing sizes too (ie: leaderboard etc), so if you are able to show your design in a few different sizes, that would be great.

We don't have alot of images for you to work off, so it will be your creative design skills that make it great.

Please keep in mind this is for a massive event that we will be competing with alot of other businesses for, as it is an annual event where the whole country goes on sale. We are in the process of building a photo studio so we have attached the images we have to work with now.

I have uploaded some of our patterns for you. This is CONFIDENTIAL. You are welcome to use these patterns in the dsign if you like.

Please, do your best.

Urban mums who crave design and function more than a cheap product.

Baby

• montserrat; intro rust; Pirou

b768aa
e667a6
f68e4e
fece3e
fbf289
add136
cadf82
33b8a4
33a6d7

• One, or both, of the two images upload. They are: IMG.5251 / IMG. 5253
• Would love a toddler in the pic also, if possible...they don't have to be using our beanbag, but there should be a pic of our beanbag there, as if it is waiting for them to use.
• Other brands. Childish themes. Too much vector overload...but some is awesome.

```html
<!DOCTYPE html>
<html lang="en">
<head>
<meta charset="utf-8">
<title>EOFYS Sale Banner</title>
<link href="https://fonts.googleapis.com/css2?family=Montserrat:wght@600;700&display=swap" rel="stylesheet">
<style>
  :root {
    --stage: #e6e6e6;
    --paper: #ffffff;
    --paper-shade: #f1f1f1;
    --ink: #111111;
    --coral: #f58585;
    --coral-deep: #f38a8a;
    --blush: #fcd2d2;
    --blush-soft: #fde6e6;
    --photo-warm: #d9cfc8;
    --photo-cool: #cfcfd4;
    --product: #efe3dc;
  }
  html, body {
    margin: 0;
    width: 1200px;
    height: 1200px;
    overflow: hidden;
    background: var(--stage);
  }
  .banner {
    position: absolute;
    left: 166px;
    top: 42px;
    width: 700px;
    height: 900px;
    transform: scale(1.24);
    transform-origin: 0 0;
    background: linear-gradient(180deg, var(--paper) 0%, var(--paper-shade) 100%);
    overflow: hidden;
    font-family: "Montserrat", sans-serif;
  }
  .banner__art {
    position: absolute;
    inset: 0;
  }
  .headline {
    position: absolute;
    left: 40px;
    top: 70px;
    margin: 0;
    font-weight: 700;
    line-height: 1.05;
    color: var(--ink);
  }
  .headline span { display: block; }
  .headline__top { font-size: 33px; letter-spacing: 0.5px; }
  .headline__mid { font-size: 47px; color: var(--coral); font-weight: 600; }
  .headline__bottom { font-size: 39px; }
  .offer {
    position: absolute;
    left: 60px;
    top: 658px;
    width: 570px;
    height: 160px;
    border-radius: 22px;
    background: linear-gradient(180deg, #ffffff 0%, var(--blush-soft) 35%, var(--blush) 100%);
    box-shadow: 0 14px 18px -12px rgba(0,0,0,0.25);
    display: flex;
    flex-direction: column;
    justify-content: center;
    align-items: center;
    text-align: center;
    font-weight: 700;
    font-size: 38px;
    line-height: 1.13;
    color: var(--ink);
  }
  .offer__highlight { color: var(--coral); font-weight: 600; }
  .footer-band {
    position: absolute;
    left: 0;
    bottom: 0;
    width: 700px;
    height: 30px;
    background: var(--coral-deep);
  }
</style>
</head>
<body>
  <main class="banner">
    <svg class="banner__art" viewBox="0 0 700 900" width="700" height="900">
      <defs>
        <linearGradient id="hero-photo" x1="0" y1="0" x2="1" y2="1">
          <stop offset="0" stop-color="#ecebea"/>
          <stop offset="0.6" stop-color="var(--photo-warm)"/>
          <stop offset="1" stop-color="#b9aca4"/>
        </linearGradient>
        <linearGradient id="toddler-photo" x1="0" y1="0" x2="0" y2="1">
          <stop offset="0" stop-color="var(--photo-cool)"/>
          <stop offset="1" stop-color="#bfb3ad"/>
        </linearGradient>
        <linearGradient id="reading-photo" x1="0" y1="0" x2="0" y2="1">
          <stop offset="0" stop-color="#e3e3e6"/>
          <stop offset="1" stop-color="#8c7d74"/>
        </linearGradient>
        <radialGradient id="product-shot" cx="0.5" cy="0.5" r="0.55">
          <stop offset="0" stop-color="#f4e6ee"/>
          <stop offset="1" stop-color="var(--product)"/>
        </radialGradient>
      </defs>

      <path class="hero-photo" role="img" aria-label="Photo of a mother playing with her baby lying in a beanbag"
            d="M300,0 H700 V350 C610,345 520,338 440,328 C360,300 300,200 300,0 Z"
            fill="url(#hero-photo)"/>
      <path class="hero-frame" d="M262,0 H300 C300,200 360,300 440,328 C520,338 610,345 700,350 V358 C600,362 500,356 430,345 C320,310 262,200 262,0 Z"
            fill="var(--blush)"/>

      <path class="wave-band" d="M0,300 C80,228 180,228 280,278 C340,308 400,345 450,357 L452,346 C400,332 340,298 280,262 C180,212 80,214 0,268 Z"
            fill="var(--blush)"/>
      <path class="wave-line" d="M0,304 C80,232 180,232 280,282 C340,312 400,348 450,360"
            fill="none" stroke="var(--coral-deep)" stroke-width="5"/>

      <ellipse class="product-shot" role="img" aria-label="Product photo of a baby resting in a patterned beanbag with rocker base"
               cx="215" cy="470" rx="175" ry="145" fill="url(#product-shot)"/>

      <circle class="lifestyle-photo" role="img" aria-label="Photo of a toddler sitting on a beanbag in a nursery"
              cx="535" cy="345" r="100" fill="url(#toddler-photo)" stroke="var(--coral-deep)" stroke-width="6"/>
      <circle class="lifestyle-photo" role="img" aria-label="Photo of a girl reading beside a baby on beanbags"
              cx="535" cy="533" r="102" fill="url(#reading-photo)" stroke="var(--coral-deep)" stroke-width="6"/>
    </svg>

    <h1 class="headline">
      <span class="headline__top">THE EOFYS</span>
      <span class="headline__mid">SALE IS</span>
      <span class="headline__bottom">ON NOW!</span>
    </h1>

    <div class="offer">
      <span>30% OFF ALL ORDERS</span>
      <span class="offer__highlight">OVER $149 WITH</span>
      <span>CODE: EOFYS</span>
    </div>

    <div class="footer-band"></div>
  </main>
</body>
</html>
```